Whitcombe MD Crest Primary Care Business Card

Need a business card for a medical clinic targeting VIP patients. Should portray an upscale feeling. Simple, clean design. Logo and colors need to be incorporated into card. Clinic colors are gray/ silver, blues, white same as logo.
Clinic is a cash only VIP service clinic targeting higher income patients.
Tagline: "Personal care for every patient, every visit"

Target Market(s)

VIP, upscale

Industry/Entity Type

Medical

Contact Information for Business Card

Would like to use for cards with raised print or metallic highlight.

Requirements
Must have
• Incorporate logo, Use colors in logo
Nice to have
• Metallic detail
Should not have
• too much details or colors, other stock photos or designs

```html
<!DOCTYPE html>
<html lang="en">
<head>
<meta charset="utf-8">
<title>Whitcombe MD Crest Primary Care – Business Card</title>
<link rel="stylesheet" href="https://fonts.googleapis.com/css2?family=Cinzel:wght@400;500&family=Open+Sans:wght@400;500&display=swap">
<style>
  :root {
    --stage: #e4e5e7;
    --card-white: #ffffff;
    --slate: #3e4f63;
    --navy-ink: #2f3d52;
    --gray-text: #7d8389;
    --silver: #a9aeb3;
  }
  * { margin: 0; padding: 0; box-sizing: border-box; }
  html, body {
    width: 1200px; height: 1000px; overflow: hidden;
    background: var(--stage);
  }
  .canvas { position: relative; width: 1200px; height: 1000px; }

  .card {
    position: absolute; left: 266px; width: 666px; height: 396px;
    box-shadow: 0 3px 8px rgba(0,0,0,0.18);
  }
  .card-front { top: 74px; background: var(--card-white); }
  .card-back { top: 534px; background: var(--slate); }

  .brand-mark {
    position: absolute; left: 50%; transform: translateX(-50%);
    border-radius: 50%;
  }
  .card-front .brand-mark { top: 50px; width: 100px; height: 100px; background: var(--slate); }
  .card-back .brand-mark { top: 80px; width: 150px; height: 150px; background: var(--silver); }

  .brand-name {
    position: absolute; left: 0; right: 0; text-align: center;
    font-family: "Cinzel", serif; font-weight: 500; text-transform: uppercase;
    letter-spacing: 0.5px;
  }
  .card-front .brand-name { top: 168px; color: var(--navy-ink); font-size: 21px; line-height: 27px; }
  .card-back .brand-name { top: 248px; color: var(--silver); font-size: 29px; line-height: 38px; }

  .holder {
    position: absolute; right: 349px; top: 244px; text-align: right;
    font-family: "Open Sans", sans-serif; white-space: nowrap;
  }
  .holder-name {
    font-family: "Cinzel", serif; font-weight: 500; text-transform: uppercase;
    color: var(--navy-ink); font-size: 17px; line-height: 24px; letter-spacing: 0.5px;
  }
  .holder-role { color: var(--gray-text); font-size: 15px; line-height: 22px; }
  .holder-address { color: var(--gray-text); font-size: 15px; margin-top: 22px; }

  .divider {
    position: absolute; left: 332px; top: 246px; width: 1.5px; height: 86px;
    background: var(--navy-ink);
  }

  .contact-list {
    position: absolute; left: 347px; top: 244px; list-style: none;
    font-family: "Open Sans", sans-serif; color: var(--gray-text); font-size: 15px;
    white-space: nowrap;
  }
  .contact-list li { display: flex; align-items: center; height: 22.5px; }
  .contact-list svg { width: 15px; height: 13px; margin-right: 7px; fill: var(--navy-ink); flex: none; }

  .tagline-band {
    position: absolute; left: 0; right: 0; bottom: 0; height: 37px;
    background: var(--slate); color: #ffffff; text-align: center;
    font-family: "Open Sans", sans-serif; font-size: 16px; line-height: 31px;
  }
</style>
</head>
<body>
<main class="canvas">
  <section class="card card-front">
    <div class="brand-mark" aria-hidden="true"></div>
    <p class="brand-name">Whitcombe MD<br>Crest Primary Care</p>

    <div class="holder">
      <p class="holder-name">Marissa Thornwell</p>
      <p class="holder-role">Managing Director</p>
      <p class="holder-address">418 Harlow Ave, Brookfield, NY 10452</p>
    </div>
    <div class="divider"></div>
    <ul class="contact-list">
      <li><svg viewBox="0 0 16 14"><path d="M1 4c0-2 3-3 7-3s7 1 7 3v1h-3V4H4v1H1z"/><rect x="3" y="6" width="10" height="7" rx="1"/></svg>+ 000 000 0000</li>
      <li><svg viewBox="0 0 16 14"><rect x="4" y="0" width="8" height="4"/><rect x="0" y="5" width="16" height="6" rx="1"/><rect x="4" y="9" width="8" height="5"/></svg>+ 000 000 0000</li>
      <li><svg viewBox="0 0 16 14"><path d="M0 2h16v1L8 8 0 3z"/><path d="M0 5l8 5 8-5v7H0z"/></svg>info@whitcombemdcrestpc.com</li>
      <li><svg viewBox="0 0 16 14"><circle cx="8" cy="7" r="6.5"/></svg>www.whitcombemdcrestpc.com</li>
    </ul>

    <p class="tagline-band">Personal care for every patient, every visit</p>
  </section>

  <section class="card card-back">
    <div class="brand-mark" aria-hidden="true"></div>
    <p class="brand-name">Whitcombe MD<br>Crest Primary Care</p>
  </section>
</main>
</body>
</html>
```